Webpage for co-working space for tech startups

We have an established co-working space in Aalborg Denmark where we have around 30 companies sharing office space. We are starting a new chapter for us and would like to have a new graphical image - new logo and new webpage, but keep the same name. The webpage should be professional, but also "fun", not too serious. We are all about working hard on our companies, but also taking some time off in between and being social and having fun. We are not corporate, but want to project the image that we are serious about what we do.

We currently have a black/red logo (see www.pebblehive.dk or test.pebblehive.dk), but are interesting in having a new logo design, so colour can be chosen freely. Currently our logo is a big PEBBLE and a little hive underneath the PEBBLE. The new logo will be one word "pebblehive" with a small logo before or on top.

If we can make a good webpage for this project, then I have a second more simple project which is also a small single page wordpress site which I would also like to have made.

Target Market(s)

tech startups - relatively new companies, typically younger people 20-35 with a tech background - business or programming, preferably both

Industry/Entity Type

PEBBLE

Logo Text

pebblehive

Coding

Coded - Design and coding required

Number of Pages Required

4 page

Font styles to use
Sans Serif

Colors

Designer to choose colors to be used in the design.

Requirements
Must have
• Wordpress CMS.
• Mobile and PC optimized
• 2 languages - English and Danish
• Four sections, could be four pages, or four sections of a single page.
• "Home", "Residents", "Our Working Space", "Our Event Space"
• Footer of page or pages should have contact information.
• "Home" has some information about who we are and what we do
• "Residents" has a list of all our residents - it should be possible to easily add and removed new / old residents - See one example here: http://test.pebblehive.dk/en_GB/beboere/ or another example here: http://www.pebblehive.dk/beboere/ - one of our colleagues http://quillbarn.dk/startups/ or another one of our colleagues http://www.copperdeckhall.dk/residents/
• "Our working space" will have a description of our building, a map of where it is and a bunch of photos which show the different offices, meeting rooms and people working
• "Our events space" will have a description of our event spaces, details of cost + different arrangments of furniture, and lots of photos of events, see here for an example http://www.pebblehive.dk/lej-vores-lokaler/
• Our current webpage - www.pebblehive.dk was put together very quickly and has not really been optimized. We started a new webpage test.pebblehive.dk, but it was never really finished.
• We are looking for a simple webpage, not too much going on. Examples of some of our colleagues in the business http://quillbarn.dk/, http://www.copperdeckhall.dk/,
Nice to have
• http://www.copperdeckhall.dk/ is a really good template for us. If we can get something like this, we are happy.

```html
<!DOCTYPE html>
<html lang="en">
<head>
<meta charset="utf-8">
<title>PEBBLEhive – Co-working Space</title>
<link href="https://fonts.googleapis.com/css2?family=Lato:wght@300;400;700;900&display=swap" rel="stylesheet">
<style>
:root{
  --blue:#2ea3dc;
  --blue-dark:#1f86bd;
  --ink:#3a3a3a;
  --text:#555;
  --paper:#f4f4f4;
  --white:#fff;
  --footer:#2b2b2b;
  --footer-line:#444;
}
*{margin:0;padding:0;box-sizing:border-box}
html,body{width:1200px;height:4534px;overflow:hidden}
body{font-family:"Lato",Arial,sans-serif;color:var(--text);background:var(--paper);position:relative}
.abs{position:absolute}
.btn{position:absolute;background:var(--blue);color:var(--white);font-size:13px;font-weight:700;letter-spacing:.5px;text-transform:uppercase;display:flex;align-items:center;justify-content:center}
.btn--ghost{background:var(--white);color:var(--ink);border:1px solid #ccc}
.photo{position:absolute}

/* hero */
.hero{position:absolute;left:0;top:0;width:1200px;height:660px;background:linear-gradient(135deg,#9a938c 0%,#6f6a66 40%,#4a4744 75%,#8e8880 100%)}
.hero__shade{position:absolute;inset:0;background:rgba(20,20,20,.35)}
.brand{position:absolute;display:flex;align-items:center;gap:8px;color:var(--white);font-weight:900;font-size:26px;letter-spacing:1px}
.brand__mark{width:18px;height:18px;background:var(--blue)}
.brand small{font-size:13px;font-weight:400;letter-spacing:4px;display:block;line-height:1}
.lang{position:absolute;left:930px;top:36px;width:80px;height:24px;border:1px solid rgba(255,255,255,.8);color:var(--white);font-size:11px;display:flex;align-items:center;justify-content:center;gap:6px}
.hero__kicker{position:absolute;left:293px;top:236px;color:var(--white);font-size:34px;font-weight:700;letter-spacing:1px}
.hero__title{position:absolute;left:290px;top:272px;color:var(--white);font-size:62px;font-weight:700;letter-spacing:1px}
.hero__lead{position:absolute;left:293px;top:356px;width:620px;color:var(--white);font-size:12px;line-height:1.5}
.mouse{position:absolute;left:590px;top:590px;width:18px;height:30px;border:2px solid var(--white);border-radius:9px}
.mouse::after{content:"";position:absolute;left:6px;top:5px;width:2px;height:7px;background:var(--white)}

/* nav */
.nav{position:absolute;left:0;top:660px;width:1200px;height:65px;background:var(--blue);display:flex;padding-left:423px}
.nav a{color:var(--white);text-decoration:none;font-size:14px;padding:0 16px;display:flex;align-items:center}
.nav a.is-active{background:var(--blue-dark)}

/* headings */
.h-section{position:absolute;font-size:44px;font-weight:700;color:var(--ink);letter-spacing:1px}
.h-section span{color:var(--blue)}
.h-center{left:0;width:1200px;text-align:center}
.para{position:absolute;font-size:12px;line-height:1.55;color:var(--text)}
.text-block{position:absolute;font-size:12px;line-height:1.55;color:var(--text)}
.text-block p + p{margin-top:16px}

/* offset frames */
.frame{position:absolute;background:var(--blue)}

/* facilities */
.feature{position:absolute;width:260px}
.feature__head{display:flex;align-items:flex-end;gap:12px;color:var(--ink);font-size:13px;text-transform:uppercase}
.feature__head svg{width:40px;height:32px;stroke:var(--blue);fill:none;stroke-width:2}
.feature p{font-size:13px;line-height:1.4;margin-top:6px;color:var(--text)}

/* band */
.band{position:absolute;left:0;top:2926px;width:1200px;height:360px;background:linear-gradient(120deg,#59b8e6,#2ea3dc 50%,#1d8fcb)}
.band__title{position:absolute;left:0;top:2998px;width:1200px;text-align:center;color:var(--white);font-size:40px;font-weight:700;line-height:1.2}
.band__lead{position:absolute;left:0;top:3106px;width:1200px;text-align:center;color:var(--white);font-size:14px}

/* events */
.card{position:absolute;top:3461px;width:397px;height:460px;background:var(--white)}
.card__photo{width:100%;height:248px}
.card__title{text-align:center;color:var(--blue);font-size:30px;font-weight:700;margin-top:22px}
.card__sub{text-align:center;color:var(--ink);font-size:15px;margin-top:6px}
.card__price{text-align:center;color:var(--blue);font-size:13px;margin-top:6px}
.card__text{text-align:center;font-size:14px;line-height:1.4;margin:14px 60px 0}
.note{position:absolute;left:190px;top:3944px;font-size:13px;color:var(--text)}
.note b{color:var(--blue);font-weight:400}
.rule{position:absolute;left:190px;top:3970px;width:817px;height:1px;background:#d6d6d6}

/* partners */
.partner{position:absolute;top:4140px;display:flex;align-items:center;gap:8px;font-size:18px;font-weight:700;color:#2c3e66}
.partner i{width:16px;height:16px;background:#2c3e66;display:block}

/* footer */
.footer{position:absolute;left:0;top:4241px;width:1200px;height:293px;background:var(--footer)}
.foot-col{position:absolute;top:4352px;color:var(--white)}
.foot-col h4{font-size:17px;font-weight:900;letter-spacing:1px;margin-bottom:12px}
.foot-col a{display:block;color:var(--blue);font-size:13px;text-decoration:none;line-height:1.25}
.subscribe{position:absolute;left:735px;top:4384px;width:280px;height:28px;background:var(--white);font-size:12px;color:#888;display:flex;align-items:center;padding-left:10px}
.subscribe span{position:absolute;right:0;top:0;width:40px;height:28px;background:var(--blue);display:flex;align-items:center;justify-content:center}
.foot-social{position:absolute;left:735px;top:4424px;display:flex;align-items:center;gap:8px;color:var(--blue);font-size:12px}
.foot-social i{width:16px;height:16px;background:var(--blue);display:block}
.foot-rule{position:absolute;left:190px;top:4478px;width:825px;height:1px;background:var(--footer-line)}
.copyright{position:absolute;left:0;top:4488px;width:1200px;text-align:center;color:#ccc;font-size:12px}
</style>
</head>
<body>

<!-- Hero -->
<section class="hero" role="img" aria-label="Photo of hands typing on a keyboard at a desk with a monitor">
  <div class="hero__shade"></div>
</section>
<div class="brand" style="left:187px;top:22px">
  <span class="brand__mark"></span>
  <div>PEBBLE<small>hive</small></div>
</div>
<div class="lang"><span>EN</span><span>|</span><span>DA</span></div>
<div class="hero__kicker">STARTUP</div>
<h1 class="hero__title">CO-WORKING SPACE</h1>
<p class="hero__lead">Lorem Ipsum is simply dummy text of the printing and typesetting industry. Lorem Ipsum has been the industry's standard dummy text ever since the 1500s.</p>
<div class="btn" style="left:538px;top:414px;width:121px;height:36px">Join us</div>
<div class="mouse"></div>

<nav class="nav">
  <a class="is-active">Home</a><a>Residents</a><a>Our Working Space</a><a>Our Event Space</a>
</nav>

<!-- About -->
<h2 class="h-section" style="left:190px;top:846px"><span>ABOUT</span> STARTUP</h2>
<div class="text-block" style="left:190px;top:918px;width:375px">
  <p>The corporate community at PEBBLEhive is a community of tech entrepreneurs with global growth ambitions. The vision is to create the best possible conditions for North Jutland entrepreneurs by offering them an environment where they can share knowledge, experience, resources, ideas, motivation and inspiration daily.</p>
  <p>With its 2,200 m2, PEBBLEhive can offer both individual offices, flexspaces, meeting rooms, community rooms and smaller prototype workshops. Common to companies is their global ambitions and scalable potential.</p>
</div>
<div class="btn" style="left:187px;top:1148px;width:136px;height:36px">Read more</div>
<div class="frame" style="left:584px;top:812px;width:423px;height:372px"></div>
<div class="photo" style="left:598px;top:798px;width:409px;height:372px;background:linear-gradient(160deg,#6d5a47,#3b3632 55%,#b9b6b0)" role="img" aria-label="Photo from above of people working on laptops at a wooden table"></div>

<!-- Resident -->
<div class="frame" style="left:176px;top:1311px;width:412px;height:369px"></div>
<div class="photo" style="left:190px;top:1297px;width:412px;height:369px;background:linear-gradient(180deg,#9fc0dc 0%,#c8d6e2 40%,#8a3f33 58%,#6c5a48 80%,#5f7a3a 100%)" role="img" aria-label="Photo of a historic red half-timbered building with a lawn"></div>
<h2 class="h-section" style="left:650px;top:1306px">RESIDENT</h2>
<div class="abs" style="left:650px;top:1400px;color:var(--blue);font-size:17px;font-weight:700">KERNEN IN PEBBLEHIVE</div>
<div class="text-block" style="left:650px;top:1432px;width:370px">
  <p>At PEBBLEhive we do not call the companies at the castle tenants – they are so much more than that. They are inhabitants. These are the ones that help create the right atmosphere. They all have equal to the community. They all have something unique to contribute, and although everyone is doing something widely different, residents have their global ambitions and scalable potential in common.</p>
  <p>Learn more about what we offer residents.</p>
</div>
<div class="btn" style="left:650px;top:1647px;width:133px;height:36px">Learn more</div>

<!-- Working space -->
<h2 class="h-section h-center" style="top:1826px">OUR WORKING SPACE</h2>
<div class="photo" style="left:290px;top:1917px;width:303px;height:184px;background:linear-gradient(180deg,#b9cde0,#8b4236 55%,#5f7a3a)" role="img" aria-label="Photo of the building front with a tree"></div>
<div class="photo" style="left:605px;top:1917px;width:296px;height:184px;background:linear-gradient(180deg,#9bb7d3,#8a3f33 55%,#61803c)" role="img" aria-label="Photo of the building wing and courtyard"></div>
<div class="photo" style="left:290px;top:2113px;width:303px;height:184px;background:linear-gradient(135deg,#1f3f66,#3f6e92 50%,#1a3558)" role="img" aria-label="Aerial site plan of the building grounds"></div>
<div class="photo" style="left:605px;top:2113px;width:296px;height:184px;background:linear-gradient(180deg,#2b2b2b,#4a2620 55%,#2d3a22)" role="img" aria-label="Darkened photo of the building with an expand icon"></div>
<svg class="abs" style="left:738px;top:2190px" width="30" height="30" viewBox="0 0 30 30" fill="none" stroke="#fff" stroke-width="2.5"><path d="M2 10V2h8M20 2h8v8M28 20v8h-8M10 28H2v-8"/></svg>

<!-- Facilities -->
<h2 class="h-section h-center" style="top:2434px">WORK SPACE FACILITIES</h2>
<div class="feature" style="left:187px;top:2540px">
  <div class="feature__head"><svg viewBox="0 0 40 32"><path d="M4 12a23 23 0 0 1 32 0M9 17a16 16 0 0 1 22 0M14 22a9 9 0 0 1 12 0"/><circle cx="20" cy="27" r="2"/></svg>Highspeed Internet</div>
  <p>Lorem Ipsum is simply dummy text of the printing and typesetting industry.</p>
</div>
<div class="feature" style="left:514px;top:2540px">
  <div class="feature__head"><svg viewBox="0 0 40 32"><path d="M6 10h22v12a6 6 0 0 1-6 6h-10a6 6 0 0 1-6-6z M28 13h4a4 4 0 0 1 0 8h-4M12 3v4M18 3v4"/></svg>Free Coffe Everyday</div>
  <p>Lorem Ipsum is simply dummy text of the printing and typesetting industry.</p>
</div>
<div class="feature" style="left:807px;top:2540px">
  <div class="feature__head"><svg viewBox="0 0 40 32"><path d="M10 9h20a7 7 0 0 1 7 9l-2 6a3 3 0 0 1-5 1l-4-4h-12l-4 4a3 3 0 0 1-5-1l-2-6a7 7 0 0 1 7-9zM12 14v6M9 17h6"/><circle cx="27" cy="15" r="1"/><circle cx="30" cy="18" r="1"/></svg>Game Station</div>
  <p>Lorem Ipsum is simply dummy text of the printing and typesetting industry.</p>
</div>
<div class="feature" style="left:187px;top:2673px">
  <div class="feature__head"><svg viewBox="0 0 40 32"><path d="M3 6h20v12H11l-5 4v-4H3zM27 12h10v12h-3v4l-5-4h-8v-3"/></svg>Meeting Room</div>
  <p>Lorem Ipsum is simply dummy text of the printing and typesetting industry.</p>
</div>
<div class="feature" style="left:514px;top:2673px">
  <div class="feature__head"><svg viewBox="0 0 40 32"><path d="M3 6h34v18H3zM20 24v5M13 29h14"/></svg>Conference Room</div>
  <p>Lorem Ipsum is simply dummy text of the printing and typesetting industry.</p>
</div>
<div class="feature" style="left:807px;top:2673px">
  <div class="feature__head"><svg viewBox="0 0 40 32"><path d="M3 4h34v26H3zM14 4v26M26 4v26M3 9h34M9 15v4M20 15v4M31 15v4"/></svg>Dedicated Lockers</div>
  <p>Lorem Ipsum is simply dummy text of the printing and typesetting industry.</p>
</div>
<div class="btn" style="left:514px;top:2811px;width:172px;height:39px">Explore all facilities</div>

<!-- Band -->
<section class="band" role="img" aria-label="Blue tinted photo of a modern office space"></section>
<h2 class="band__title">Our Modern Office Spaces<br>Are Simply Stunning</h2>
<p class="band__lead">Lorem Ipsum is simply dummy text of the printing and typesetting industry.</p>
<div class="btn btn--ghost" style="left:538px;top:3171px;width:127px;height:36px">Book a tour</div>

<!-- Event space -->
<h2 class="h-section h-center" style="top:3354px">OUR EVENT SPACE</h2>
<article class="card" style="left:190px">
  <div class="card__photo" style="background:linear-gradient(135deg,#c9b9a6,#8b6b52 50%,#e2ddd6)" role="img" aria-label="Photo of two guests chatting at an event"></div>
  <div class="card__title">DAY EVENT</div>
  <div class="card__sub">Lounge Area</div>
  <div class="card__price">Rent Of The Lounge: 500,- Ex Moms</div>
  <p class="card__text">Morning meeting for 30 guests. We serve you breakfast, water, organic tea and coffee from our in-house barista to get you on your feet.</p>
</article>
<article class="card" style="left:611px">
  <div class="card__photo" style="background:linear-gradient(135deg,#f1f1ef,#d8d6d0 50%,#9a9287)" role="img" aria-label="Photo of champagne glasses set on a table for a reception"></div>
  <div class="card__title">STANDING RECEPTION</div>
  <div class="card__sub">Canteen Area</div>
  <div class="card__price">Rent Of The Canteen: 500,- Ex Moms</div>
  <p class="card__text">When you have something to celebrate for 50 guests. Light fingerfood, wine, and non-alcoholic refreshments are included.</p>
</article>
<p class="note"><b>NOTE :</b> If you need to rent the premises for a shorter period or in the evening hours, the hourly rate is 475,- ex VAT.</p>
<div class="rule"></div>
<div class="btn" style="left:520px;top:4005px;width:157px;height:39px">View more events</div>

<!-- Partners -->
<div class="partner" style="left:190px"><i></i>RIDGEWAY</div>
<div class="partner" style="left:425px;color:#c0392b">MARLOW &amp; CO</div>
<div class="partner" style="left:680px;font-size:15px;color:#1d3a6b"><i style="background:#1d3a6b"></i>Nordvik Bank</div>
<div class="partner" style="left:912px;font-size:14px;color:#333">HANNE LUND</div>

<!-- Footer -->
<footer class="footer"></footer>
<div class="brand" style="left:543px;top:4268px">
  <span class="brand__mark"></span>
  <div>PEBBLE<small>hive</small></div>
</div>
<div class="foot-col" style="left:190px"><h4>ABOUT</h4><a>About Us</a><a>Contact Us</a><a>F.A.Q</a><a>Privacy</a></div>
<div class="foot-col" style="left:390px"><h4>SPACE</h4><a>Resident</a><a>Working Space</a><a>Event Space</a></div>
<div class="foot-col" style="left:592px"><h4>LEGAL</h4><a>Privacy</a><a>Terms</a><a>Advertise</a><a>Sponsors</a></div>
<div class="foot-col" style="left:735px"><h4>SUBSCRIBE</h4></div>
<div class="subscribe">E-Mail Address<span><svg width="16" height="14" viewBox="0 0 16 14"><path d="M1 7L15 1 11 13 8 8z" fill="#fff"/></svg></span></div>
<div class="foot-social"><i></i>community.pebblehive.dk/aalborg</div>
<div class="foot-rule"></div>
<p class="copyright">© Copyright 2018 - pebble.All Right Reserved</p>

</body>
</html>
```